Luxury Wine Label for New Startup Winery

We need a wine label for our new winery startup. We have worked with a local designer but do not feel the resulting label / logo have the elevation required to present our brand as a luxury wine. Our winery is called "Harrowgate Vineyards" and we are focused on extremely high quality hand crafted artisan and estate wines from the Pacific Northwest.
We would like to see designs that utilize a tree line, or other imagery that represents the "Harrowgate" part of our company name. Another interesting feature could be wood grain.
A logo will be required based on your design so please design with this in mind:
This logo should be consistent with the wine bottle label design, and should be representative of our high end exclusive wine while giving a sense of place (Oregon/ Pacific Northwest.)
I will supply an image of the design we received from our local designer, PLEASE NOTE: in general we do like wood grain and tree line concepts but feel the execution was poorly done.
ATTN: Logo design should be suitable for use on: Bottles (Red wine/rose/white wine), Bussiness cards, vehicle signage, business signage, etc
P.S.:
If you have a design that is not outside the box we are still interested in seeing it.
Label is for a burgundy style bottle with a label height of 3.5 - 4" and a width of 3.5-4"
any label <= 4"x4" and >=3.5"x3.5" will be acceptable:
HOWEVER Width should be greater than or equal to height due to the bottle format
Target Market(s)
Wine enthusiasts with adequate discretionary budgets to afford $100 bottles of wine.
Industry/Entity Type
Wine / Winery
Requirements
Must have
- A sense of luxury, a feel of exclusivity, and a theme consistent with our product and brand name
Nice to have
- Tree line, wood grain or other wood themes. Serif fonts
Should not have
- anything cheesy, off topic, hard to read script fonts or anything that makes the label hard to read from a few feet away or too busy

```html
<!DOCTYPE html>
<html lang="en">
<head>
<meta charset="utf-8">
<title>Harrowgate Vineyards – Syrah Label</title>
<link rel="stylesheet" href="https://fonts.googleapis.com/css2?family=Cinzel:wght@400;500;600&family=Montserrat:wght@400;500&family=Cormorant+Garamond:wght@500&display=swap">
<style>
  :root {
    --backdrop: #e4e4e4;
    --label-black: #1c1c1b;
    --label-charcoal: #2a2a28;
    --gold-light: #f3dc94;
    --gold: #c9a250;
    --gold-deep: #8a6a2c;
    --ivory: #ece8de;
    --muted: #b9b4a8;
  }
  * { box-sizing: border-box; margin: 0; padding: 0; }
  html, body {
    width: 1200px;
    height: 1200px;
    overflow: hidden;
    background: var(--backdrop);
  }
  .canvas {
    width: 1200px;
    height: 1200px;
    display: flex;
    align-items: center;
    justify-content: center;
  }
  .wine-label {
    position: relative;
    width: 760px;
    height: 760px;
    background: linear-gradient(180deg, var(--label-charcoal) 0%, var(--label-black) 60%);
    display: flex;
    flex-direction: column;
    align-items: center;
  }
  .label-frame {
    position: absolute;
    inset: 24px;
    border: 3px solid var(--gold);
    pointer-events: none;
  }
  .mountain-scene {
    margin-top: 60px;
    width: 620px;
    height: 330px;
    background: linear-gradient(180deg, #3a3934 0%, #2c2b28 55%, #4a3d22 80%, #8a6a2c 100%);
    border-bottom: 2px solid var(--gold);
  }
  .brand-name {
    margin-top: 46px;
    font-family: "Cinzel", serif;
    font-weight: 500;
    font-size: 66px;
    letter-spacing: 4px;
    color: var(--gold);
    line-height: 1;
  }
  .brand-descriptor {
    margin-top: 16px;
    font-family: "Montserrat", sans-serif;
    font-weight: 500;
    font-size: 24px;
    letter-spacing: 9px;
    color: var(--muted);
  }
  .varietal {
    margin-top: 30px;
    font-family: "Cinzel", serif;
    font-weight: 500;
    font-size: 48px;
    letter-spacing: 3px;
    color: var(--ivory);
  }
  .appellation {
    margin-top: 54px;
    font-family: "Cormorant Garamond", serif;
    font-weight: 500;
    font-size: 16px;
    letter-spacing: 2px;
    color: var(--muted);
  }
  .base-rule {
    position: absolute;
    left: 24px;
    right: 24px;
    bottom: 62px;
    height: 3px;
    background: linear-gradient(90deg, var(--gold-deep), var(--gold-light), var(--gold), var(--gold-deep));
  }
</style>
</head>
<body>
  <main class="canvas">
    <section class="wine-label">
      <div class="label-frame"></div>
      <div class="mountain-scene" role="img" aria-label="Gold-outlined mountain range with a stand of golden fir trees along the horizon"></div>
      <h1 class="brand-name">Harrowgate</h1>
      <p class="brand-descriptor">VINEYARDS</p>
      <h2 class="varietal">SYRAH</h2>
      <p class="appellation">WILLAMETTE VALLEY / 2024</p>
      <div class="base-rule"></div>
    </section>
  </main>
</body>
</html>
```